Manufacturing company needs new business card.

I need a unique Business Card that will truly stand out. Nothing too busy. Simple is good, right? Not looking for a standard design either. No cookie cutter layout. I am just looking for something interesting and a bit different. Does't have to completely off the wall crazy, just not your run of the mill business card. Clean and modern with a touch of industrial.

Target Market(s)

Air conditioning industry, Architects, builders.

Industry/Entity Type

Business

Contact Information for Business Card

Details to be included on card are:

Peter Vance
Managing Director

T: 1300 847 519
M: 0428 593 174
W: www.brenvaleworks.com.au
E: peter.vance@brenvaleworks.com.au
A: 58 Harwick Lane, Sydney NSW 2000

Font styles to use
Sans Serif

Colors
0355a3
848484
fbfbfb

Requirements
Must have
• Card design must be landscape.

```html
<!DOCTYPE html>
<html lang="en">
<head>
<meta charset="utf-8">
<title>Brenvale Works Australia – Business Card</title>
<link href="https://fonts.googleapis.com/css2?family=Lato:wght@400;700&display=swap" rel="stylesheet">
<style>
  :root {
    --brand-blue: #2c4592;
    --accent-blue: #0355a3;
    --steel-grey: #848484;
    --card-white: #fbfbfb;
    --ink: #2a2a2a;
    --band-dark: #2f3033;
    --page-bg: #ececec;
  }
  * { box-sizing: border-box; margin: 0; padding: 0; }
  html, body { width: 1200px; height: 800px; overflow: hidden; }
  body {
    background: var(--page-bg);
    font-family: "Lato", Arial, sans-serif;
    color: var(--ink);
    display: flex;
    align-items: center;
    justify-content: center;
    gap: 40px;
  }
  .card {
    position: relative;
    width: 520px;
    height: 318px;
    box-shadow: 0 6px 18px rgba(0,0,0,0.12);
    overflow: hidden;
  }
  .card--front { background: var(--card-white); }
  .card--back { background: var(--brand-blue); display: flex; align-items: center; justify-content: center; }

  .brand { display: flex; align-items: center; gap: 12px; }
  .brand__square { width: 26px; height: 26px; background: var(--brand-blue); }
  .brand__name { font-weight: 700; font-size: 25px; color: var(--brand-blue); letter-spacing: 0.2px; }
  .card--front .brand { position: absolute; left: 48px; top: 58px; }
  .card--back .brand__square { background: var(--steel-grey); width: 34px; height: 34px; }
  .card--back .brand__name { color: var(--card-white); font-size: 32px; }

  .holder { position: absolute; left: 100px; top: 140px; }
  .holder__name { font-weight: 700; font-size: 17px; letter-spacing: 0.5px; text-transform: uppercase; }
  .holder__title { font-weight: 700; font-size: 11px; color: #555; margin-top: 2px; }

  .divider { position: absolute; left: 100px; right: 0; top: 196px; height: 1.5px; background: var(--accent-blue); }

  .contacts {
    position: absolute; left: 100px; right: 20px; top: 208px;
    display: grid; grid-template-columns: 1.05fr 0.9fr 1.8fr; gap: 10px;
    font-size: 10.5px; line-height: 1.6;
  }
  .contact { display: flex; gap: 6px; align-items: flex-start; }
  .contact svg { width: 9px; height: 9px; margin-top: 3px; flex: none; fill: var(--accent-blue); }
  .contact-group { display: flex; flex-direction: column; }

  .footer-band { position: absolute; left: 0; right: 40px; bottom: 20px; height: 20px; background: var(--band-dark); }
  .footer-accent { position: absolute; right: 0; bottom: 20px; width: 40px; height: 20px; background: var(--brand-blue); }
</style>
</head>
<body>
  <section class="card card--front" aria-label="Business card front">
    <div class="brand">
      <span class="brand__square"></span>
      <span class="brand__name">Brenvale Works Australia</span>
    </div>

    <div class="holder">
      <p class="holder__name">Peter Vance</p>
      <p class="holder__title">Managing Director</p>
    </div>

    <div class="divider"></div>

    <div class="contacts">
      <div class="contact">
        <svg viewBox="0 0 10 10"><path d="M5 0a3.5 3.5 0 0 0-3.5 3.5C1.5 6 5 10 5 10s3.5-4 3.5-6.5A3.5 3.5 0 0 0 5 0zm0 5a1.5 1.5 0 1 1 0-3 1.5 1.5 0 0 1 0 3z"/></svg>
        <span>58 Harwick Lane,<br>Sydney NSW 2000</span>
      </div>
      <div class="contact-group">
        <div class="contact">
          <svg viewBox="0 0 10 10"><path d="M1 3c0-1 1-2 4-2s4 1 4 2v1H7V3H3v1H1zM2 5h6l1 4H1z"/></svg>
          <span>1300 847 519</span>
        </div>
        <div class="contact">
          <svg viewBox="0 0 10 10"><path d="M2.5 0h5v10h-5zM3.5 1v7h3V1z"/></svg>
          <span>0428 593 174</span>
        </div>
      </div>
      <div class="contact-group">
        <div class="contact">
          <svg viewBox="0 0 10 10"><path d="M0 2h10v6H0zM1 3l4 3 4-3"/></svg>
          <span>peter.vance@brenvaleworks.com.au</span>
        </div>
        <div class="contact">
          <svg viewBox="0 0 10 10"><circle cx="5" cy="5" r="4.5"/></svg>
          <span>www.brenvaleworks.com.au</span>
        </div>
      </div>
    </div>

    <div class="footer-band"></div>
    <div class="footer-accent"></div>
  </section>

  <section class="card card--back" aria-label="Business card back">
    <div class="brand">
      <span class="brand__square"></span>
      <span class="brand__name">Brenvale Works Australia</span>
    </div>
  </section>
</body>
</html>
```